Business card Zottelgarten

Business card is for a self-employed dog trainer with own dog school. Name and logo of the dog school are available. Color specifications as well. The design should be classy and minimalist, but also modern. An already existing idea would be: Front: Only the logo Back: Contact data

Font styles to use
Serif
Sans Serif
Other font styles liked:
• Trajan Pro

Colors
f78f20

Requirements
Must have
• Name: Margit Wendler-Rasch Title: Dipl. Dog Trainer Contain my logo Follow my font and color preferences (see files)

```html
<!DOCTYPE html>
<html lang="en">
<head>
<meta charset="utf-8">
<title>Zottelgarten – Business Card</title>
<link rel="stylesheet" href="https://fonts.googleapis.com/css2?family=Cinzel:wght@400;500&family=Nunito+Sans:wght@400;600&display=swap">
<style>
  :root {
    --taupe: #7d6a5c;
    --taupe-text: #6f5e52;
    --paper: #ffffff;
    --accent: #f78f20;
    --backdrop: #2b2b2d;
    --muted: #b9aca2;
  }
  * { box-sizing: border-box; margin: 0; padding: 0; }
  html, body { width: 1200px; height: 900px; overflow: hidden; }
  body {
    background: var(--backdrop);
    font-family: "Nunito Sans", sans-serif;
    position: relative;
  }
  .card {
    position: absolute;
    left: 250px;
    width: 700px;
    height: 400px;
    overflow: hidden;
    background: var(--paper);
    box-shadow: 0 14px 30px rgba(0,0,0,.45);
  }
  .card--front { top: 30px; }
  .card--back { top: 470px; }

  /* Front */
  .front-band {
    position: absolute; left: 0; top: 0; width: 100%; height: 58%;
    background: var(--taupe);
  }
  .front-mark {
    position: absolute; left: 50%; top: 38px; transform: translateX(-50%);
    width: 120px; height: 120px; border-radius: 50%;
    background: var(--paper); border: 3px solid var(--paper);
    box-shadow: 0 0 0 3px var(--taupe), 0 0 0 4px var(--paper);
  }
  .front-name {
    position: absolute; left: 0; right: 0; top: 168px; text-align: center;
    font-family: "Cinzel", serif; font-size: 40px; letter-spacing: 2px;
    color: var(--paper);
  }
  .front-url {
    position: absolute; left: 0; right: 0; top: 216px; text-align: center;
    font-family: "Cinzel", serif; font-size: 10px; letter-spacing: 6px;
    color: var(--paper);
  }

  /* Back */
  .back-head {
    position: absolute; left: 0; top: 0; width: 100%; height: 46%;
  }
  .back-name {
    position: absolute; left: 70px; top: 88px;
    font-family: "Cinzel", serif; font-size: 54px; letter-spacing: 2px;
    color: var(--taupe-text);
  }
  .back-url {
    position: absolute; left: 74px; top: 150px;
    font-family: "Cinzel", serif; font-size: 11px; letter-spacing: 8px;
    color: var(--muted);
  }
  .back-rule {
    position: absolute; left: 0; top: 184px; width: 100%; height: 3px;
    background: var(--accent);
  }
  .back-body {
    position: absolute; left: 0; top: 190px; width: 100%; bottom: 0;
    background: var(--taupe);
    padding: 22px 0 0 56px;
    color: var(--paper);
  }
  .holder-name {
    font-family: "Cinzel", serif; font-size: 20px; color: var(--accent);
    letter-spacing: .5px;
  }
  .holder-title { font-size: 15px; margin-top: 2px; }
  .contacts { list-style: none; margin-top: 22px; }
  .contacts li {
    display: flex; align-items: center; gap: 12px;
    font-size: 16px; line-height: 26px;
  }
  .contacts svg { width: 16px; height: 16px; flex: none; }
</style>
</head>
<body>
  <section class="card card--front" aria-label="Card front">
    <div class="front-band"></div>
    <div class="front-mark"></div>
    <div class="front-name">ZOTTELGARTEN</div>
    <div class="front-url">WWW.ZOTTELGARTEN.CH</div>
  </section>

  <section class="card card--back" aria-label="Card back">
    <div class="back-head">
      <div class="back-name">ZOTTELGARTEN</div>
      <div class="back-url">WWW.ZOTTELGARTEN.CH</div>
    </div>
    <div class="back-rule"></div>
    <div class="back-body">
      <div class="holder-name">MARGIT WENDLER-RASCH</div>
      <div class="holder-title">Dipl. Dog Trainer</div>
      <ul class="contacts">
        <li>
          <svg viewBox="0 0 16 16" aria-hidden="true"><circle cx="8" cy="8" r="7" fill="none" stroke="#f78f20" stroke-width="1.5"/><path d="M5.5 4.5l1.5 0.2 .6 1.8-1 .8a5 5 0 0 0 2.2 2.2l.8-1 1.8.6.2 1.5c-3 .8-6.6-2.8-6.1-6.1z" fill="#f78f20"/></svg>
          (123) 555-0147
        </li>
        <li>
          <svg viewBox="0 0 16 16" aria-hidden="true"><circle cx="8" cy="8" r="7" fill="none" stroke="#f78f20" stroke-width="1.5"/><rect x="4" y="5.2" width="8" height="5.6" rx=".6" fill="none" stroke="#f78f20" stroke-width="1.2"/><path d="M4.3 5.6L8 8.4l3.7-2.8" fill="none" stroke="#f78f20" stroke-width="1.2"/></svg>
          margit@zottelgarten.com
        </li>
        <li>
          <svg viewBox="0 0 16 16" aria-hidden="true"><circle cx="8" cy="8" r="7" fill="#f78f20"/><circle cx="8" cy="8" r="4.2" fill="none" stroke="#7d6a5c" stroke-width="1"/><path d="M3.8 8h8.4M8 3.8c-2 2.5-2 5.9 0 8.4M8 3.8c2 2.5 2 5.9 0 8.4" fill="none" stroke="#7d6a5c" stroke-width="1"/></svg>
          www.zottelgarten.ch
        </li>
      </ul>
    </div>
  </section>
</body>
</html>
```